New Business Card Design Project

Want a simple but attention grabbing business card. Back Side having mainly our logo and basic info-the front side a typical business card.

Contact Information for Business Card

Hearth & Tile Interiors
218 NW Larkspur Rd. Suite 207
Ankeny, Iowa 50021

phone- 515.482.7093

website is -htidesigns.com

```html
<!DOCTYPE html>
<html lang="en">
<head>
<meta charset="utf-8">
<title>Hearth &amp; Tile Interiors — Business Card</title>
<link rel="stylesheet" href="https://fonts.googleapis.com/css2?family=Michroma&family=Open+Sans:wght@400;600&display=swap">
<style>
  :root {
    --brand-orange: #ee6535;
    --ink-navy: #1c2a4a;
    --card-white: #fbfbfb;
    --backdrop: #d6d6d6;
    --text-white: #ffffff;
  }
  * { margin: 0; padding: 0; box-sizing: border-box; }
  html, body { width: 1200px; height: 675px; overflow: hidden; }
  body {
    background: var(--backdrop);
    font-family: "Open Sans", Arial, sans-serif;
    position: relative;
  }
  .card {
    position: absolute;
    top: 188px;
    width: 520px;
    height: 298px;
    border-radius: 18px;
    overflow: hidden;
    box-shadow: 0 6px 18px rgba(0,0,0,0.18);
  }
  .card--front { left: 60px; background: var(--card-white); }
  .card--back { left: 620px; background: var(--brand-orange); }

  .brand-name {
    position: absolute;
    left: 0; right: 0;
    text-align: center;
    font-family: "Michroma", Arial, sans-serif;
    font-weight: 400;
    letter-spacing: 1px;
    line-height: 1.25;
  }
  .card--front .brand-name { top: 56px; font-size: 24px; color: var(--brand-orange); }
  .card--back .brand-name { top: 118px; font-size: 26px; color: var(--text-white); }
  .brand-mark {
    position: absolute;
    left: 50%;
    width: 16px; height: 16px;
    margin-left: -8px;
  }
  .card--front .brand-mark { top: 30px; background: var(--brand-orange); }
  .card--back .brand-mark { top: 92px; background: var(--text-white); }

  .rule { position: absolute; height: 2px; background: var(--brand-orange); }
  .rule--top { top: 158px; left: 28px; right: 120px; }
  .rule--bottom { top: 258px; left: 230px; right: 40px; }

  .contact-list {
    position: absolute;
    left: 70px;
    top: 178px;
    width: 260px;
    color: var(--ink-navy);
    font-size: 13px;
    line-height: 22px;
    text-align: center;
  }
  .contact-row { display: flex; justify-content: center; gap: 16px; white-space: nowrap; }
  .contact-item { display: inline-flex; align-items: center; gap: 5px; }
  .contact-item svg { width: 11px; height: 11px; fill: var(--brand-orange); flex: none; }

  .person {
    position: absolute;
    right: 40px;
    top: 210px;
    text-align: right;
  }
  .person-name {
    font-family: "Michroma", Arial, sans-serif;
    font-size: 20px;
    line-height: 26px;
    color: var(--brand-orange);
    letter-spacing: 1px;
  }
  .person-title {
    font-size: 9px;
    font-weight: 600;
    letter-spacing: 1px;
    color: var(--ink-navy);
    margin-top: 2px;
  }
</style>
</head>
<body>
  <section class="card card--front" aria-label="Business card front">
    <span class="brand-mark" aria-hidden="true"></span>
    <div class="brand-name">HEARTH &amp; TILE<br>INTERIORS</div>

    <div class="rule rule--top"></div>

    <div class="contact-list">
      <div class="contact-row">
        <span class="contact-item">
          <svg viewBox="0 0 12 12" aria-hidden="true"><path d="M6 0a4 4 0 0 0-4 4c0 3 4 8 4 8s4-5 4-8a4 4 0 0 0-4-4zm0 5.5A1.5 1.5 0 1 1 6 2.5a1.5 1.5 0 0 1 0 3z"/></svg>
          Address Line 1
        </span>
      </div>
      <div class="contact-row">
        <span class="contact-item">
          <svg viewBox="0 0 12 12" aria-hidden="true"><path d="M2.5 0.5l2 2-1.2 1.5a7 7 0 0 0 4.7 4.7l1.5-1.2 2 2-1.5 2C5 11.5 0.5 7 0.5 2z"/></svg>
          Phone No.
        </span>
        <span class="contact-item">
          <svg viewBox="0 0 12 12" aria-hidden="true"><path d="M3 0h6v12H3zM4 1.5v8h4v-8z"/></svg>
          Mobile No.
        </span>
      </div>
      <div class="contact-row">
        <span class="contact-item">
          <svg viewBox="0 0 12 12" aria-hidden="true"><path d="M0 2h12v8H0zM1 3l5 3.5L11 3v-.2H1z"/></svg>
          Email ID
        </span>
        <span class="contact-item">
          <svg viewBox="0 0 12 12" aria-hidden="true"><path d="M6 0a6 6 0 1 0 0 12A6 6 0 0 0 6 0zm0 1.2c.8.9 1.3 2.5 1.4 4.2H4.6C4.7 3.7 5.2 2.1 6 1.2zM1.2 6.6h2.2c.1 1.6.5 3 1.1 4A4.8 4.8 0 0 1 1.2 6.6zm0-1.2A4.8 4.8 0 0 1 4.5 1.4c-.6 1-1 2.4-1.1 4zm3.4 1.2h2.8c-.1 1.7-.6 3.3-1.4 4.2-.8-.9-1.3-2.5-1.4-4.2zm3.9 4c.6-1 1-2.4 1.1-4h2.2a4.8 4.8 0 0 1-3.3 4zm1.1-5.2c-.1-1.6-.5-3-1.1-4a4.8 4.8 0 0 1 3.3 4z"/></svg>
          Web Address
        </span>
      </div>
    </div>

    <div class="person">
      <div class="person-name">NAME</div>
      <div class="person-title">DESIGNATION</div>
    </div>

    <div class="rule rule--bottom"></div>
  </section>

  <section class="card card--back" aria-label="Business card back">
    <span class="brand-mark" aria-hidden="true"></span>
    <div class="brand-name">HEARTH &amp; TILE<br>INTERIORS</div>
  </section>
</body>
</html>
```